Creative Brief
Stationery and Cards
Need clean, simple, modern cards/letterhead
Simple
Dale Pruett
Executive Direstor
418 Hollister Avenue
Suite 500
New York, NY 10012
Dpruett@brimlow.com
www.mistvaleloft.com

```html
<!DOCTYPE html>
<html lang="en">
<head>
<meta charset="utf-8">
<title>Mistvale – Business Cards</title>
<link href="https://fonts.googleapis.com/css2?family=Open+Sans:wght@400;600;700&display=swap" rel="stylesheet">
<style>
  :root {
    --backdrop: #e8e8e6;
    --card-dark: #1c1c1e;
    --card-dark-edge: #2a2a2d;
    --card-light: #ffffff;
    --sky: #29b8e8;
    --amber: #f5a623;
    --navy: #1f2f4a;
    --ink: #3a3a3a;
    --muted: #8a8a8a;
    --white: #ffffff;
  }
  * { box-sizing: border-box; margin: 0; padding: 0; }
  html, body {
    width: 1200px; height: 646px; overflow: hidden;
    background: var(--backdrop);
    font-family: "Open Sans", Arial, sans-serif;
  }
  .sheet {
    position: relative; width: 1200px; height: 646px;
    display: flex; align-items: center; justify-content: center; gap: 40px;
  }
  .card {
    position: relative; width: 540px; height: 308px;
    border-radius: 4px; overflow: hidden;
    box-shadow: 0 6px 18px rgba(0,0,0,.18);
  }
  /* Back of card */
  .card--back {
    background: linear-gradient(135deg, var(--card-dark-edge), var(--card-dark));
    display: flex; flex-direction: column; align-items: center; justify-content: center;
  }
  .brand { display: flex; flex-direction: column; align-items: center; }
  .brand__dot { width: 34px; height: 34px; border-radius: 50%; margin-bottom: 10px; }
  .brand__name {
    font-weight: 600; font-size: 30px; letter-spacing: 5px; text-transform: uppercase; line-height: 1;
  }
  .brand__tag {
    font-weight: 400; font-size: 8px; letter-spacing: 4px; text-transform: uppercase; margin-top: 6px;
  }
  .card--back .brand__dot { background: var(--white); }
  .card--back .brand__name { color: var(--white); }
  .card--back .brand__tag { color: #b5b5b5; }

  /* Front of card */
  .card--front { background: var(--card-light); }
  .card--front .brand { position: absolute; top: 28px; left: 0; right: 0; }
  .card--front .brand__dot { background: var(--sky); width: 30px; height: 30px; }
  .card--front .brand__name { color: var(--ink); font-size: 26px; }
  .card--front .brand__tag { color: var(--muted); }

  .info-panel {
    position: absolute; left: 0; right: 0; bottom: 0; height: 132px;
    background: var(--sky);
  }
  .accent-rule {
    position: absolute; left: 44px; right: 44px; top: 160px; height: 3px;
    background: var(--amber);
  }

  .person { position: absolute; left: 44px; top: 198px; color: var(--navy); }
  .person__name { font-weight: 700; font-size: 14px; line-height: 1.3; }
  .person__role { font-size: 10px; margin-bottom: 8px; }
  .person__line { font-size: 10px; line-height: 1.5; }

  .contacts { position: absolute; left: 330px; top: 190px; list-style: none; color: var(--navy); }
  .contacts li { display: flex; align-items: center; gap: 8px; font-size: 10px; height: 21px; }
  .contacts svg { width: 14px; height: 14px; flex: none; }
</style>
</head>
<body>
<main class="sheet">

  <section class="card card--back" aria-label="Card back">
    <div class="brand">
      <span class="brand__dot"></span>
      <span class="brand__name">Mistvale</span>
      <span class="brand__tag">Wellness Studio</span>
    </div>
  </section>

  <section class="card card--front" aria-label="Card front">
    <div class="info-panel"></div>
    <div class="accent-rule"></div>

    <div class="brand">
      <span class="brand__dot"></span>
      <span class="brand__name">Mistvale</span>
      <span class="brand__tag">Wellness Studio</span>
    </div>

    <div class="person">
      <p class="person__name">Dale Pruett</p>
      <p class="person__role">Executive Director</p>
      <p class="person__line">418 Hollister Avenue, Suite 500</p>
      <p class="person__line">New York, NY 10012</p>
    </div>

    <ul class="contacts">
      <li>
        <svg viewBox="0 0 16 16"><circle cx="8" cy="8" r="8" fill="var(--navy)"/><path d="M5.5 4.5l1.5 0 .7 2-1 .8a5 5 0 0 0 2 2l.8-1 2 .7v1.5c0 .5-.5 1-1 1A6.5 6.5 0 0 1 4.5 5.5c0-.5.5-1 1-1z" fill="var(--white)"/></svg>
        <span>917 555 0186</span>
      </li>
      <li>
        <svg viewBox="0 0 16 16"><circle cx="8" cy="8" r="8" fill="var(--navy)"/><circle cx="8" cy="6.3" r="2" fill="var(--white)"/><path d="M4.5 12a3.5 3 0 0 1 7 0z" fill="var(--white)"/></svg>
        <span>Tmorvik7</span>
      </li>
      <li>
        <svg viewBox="0 0 16 16"><circle cx="8" cy="8" r="8" fill="var(--navy)"/><rect x="4" y="5" width="8" height="6" rx=".8" fill="var(--white)"/><path d="M4.3 5.4L8 8.3l3.7-2.9" stroke="var(--navy)" stroke-width=".9" fill="none"/></svg>
        <span>Dpruett@brimlow.com</span>
      </li>
      <li>
        <svg viewBox="0 0 16 16"><circle cx="8" cy="8" r="8" fill="var(--navy)"/><circle cx="8" cy="8" r="4" stroke="var(--white)" stroke-width=".9" fill="none"/><path d="M4 8h8M8 4c-2 2.4-2 5.6 0 8M8 4c2 2.4 2 5.6 0 8" stroke="var(--white)" stroke-width=".8" fill="none"/></svg>
        <span>www.mistvaleloft.com</span>
      </li>
    </ul>
  </section>

</main>
</body>
</html>
```